Halmi Rékas Physiotherapy Business Card Vienna

We need a business card design for a newly created Physiotherapy company based in Vienna Austria.
We seek a simple, modern, minimalist design without too much color variation. The font should look young/fresh, but definitely not childish or so. Since we are a starting Business, we currently haven't got a logo, if you feel like a logo would fit your design, feel free to use one, but it's not necessary.
Target Market(s)
Healthcare, young and elderly people with mobility issues
Industry/Entity Type
Health And Wellness
Contact Information for Business Card
Name: Réka Halmi
Title description: Physiotherapist
Phone num: +43 664 5290 4116
e-mail: reka.praxis@examplemail.net
Colors
Designer to choose colors to be used in the design.
Requirements
Must have
- Final design language must be in German, basically, the Title Description needs to be "Physiotherapeutin" the other details remain as in the English Language.
Nice to have
- Simple, modern, minimalist design
Should not have
- too many colors, Obvious use of a skeleton, skull, spline

```html
<!DOCTYPE html>
<html lang="de">
<head>
<meta charset="utf-8">
<title>Réka Halmi – Physiotherapeutin</title>
<link rel="stylesheet" href="https://fonts.googleapis.com/css2?family=Kaushan+Script&family=EB+Garamond:wght@400&family=Arimo:wght@400&display=swap">
<style>
  :root {
    --forest: #3a6b04;
    --butter: #f3f092;
    --paper: #ffffff;
  }
  html, body {
    margin: 0;
    padding: 0;
    width: 1200px;
    height: 960px;
    overflow: hidden;
    background: var(--paper);
  }
  .canvas {
    position: relative;
    width: 1200px;
    height: 960px;
  }
  .business-card {
    position: absolute;
    left: 114px;
    top: 202px;
    width: 972px;
    height: 555px;
    border-radius: 19px;
    background: var(--forest);
    overflow: hidden;
  }
  .name-band {
    position: absolute;
    left: 0;
    top: 57px;
    width: 910px;
    height: 414px;
  }
  .holder-name {
    position: absolute;
    left: 60px;
    top: 60px;
    margin: 0;
    font-family: "Kaushan Script", cursive;
    font-weight: 400;
    font-size: 150px;
    line-height: 1;
    color: var(--forest);
    white-space: nowrap;
    letter-spacing: -2px;
  }
  .job-title {
    position: absolute;
    left: 90px;
    top: 270px;
    margin: 0;
    font-family: "EB Garamond", serif;
    font-weight: 400;
    font-size: 64px;
    line-height: 1;
    color: var(--forest);
    white-space: nowrap;
  }
  .contact-list {
    position: absolute;
    left: 95px;
    top: 366px;
    margin: 0;
    padding: 0;
    list-style: none;
  }
  .contact-item {
    display: flex;
    align-items: center;
    height: 38px;
    margin-bottom: 7px;
    font-family: "Arimo", sans-serif;
    font-size: 29px;
    color: var(--forest);
    white-space: nowrap;
  }
  .contact-icon {
    width: 38px;
    height: 38px;
    margin-right: 21px;
    flex: none;
  }
</style>
</head>
<body>
<div class="canvas">
  <div class="business-card">
    <svg class="name-band" viewBox="0 0 910 414" aria-hidden="true">
      <path d="M0 0 H709 A200 207 0 0 1 709 414 H0 Z" fill="var(--butter)"/>
    </svg>

    <h1 class="holder-name">Réka Halmi</h1>
    <p class="job-title">Physiotherapeutin</p>

    <ul class="contact-list">
      <li class="contact-item">
        <svg class="contact-icon" viewBox="0 0 38 38" aria-hidden="true">
          <circle cx="19" cy="19" r="19" fill="var(--forest)"/>
          <path d="M13 10 c-2 1 -3 3 -2 6 c2 5 6 9 11 11 c3 1 5 0 6 -2 l-3 -3 c-1 -1 -2 0 -3 1 c-3 -1 -6 -4 -7 -7 c1 -1 2 -2 1 -3 Z" fill="var(--butter)"/>
        </svg>
        <span class="contact-text">+43 664 5290 4116</span>
      </li>
      <li class="contact-item">
        <svg class="contact-icon" viewBox="0 0 38 38" aria-hidden="true">
          <circle cx="19" cy="19" r="19" fill="var(--forest)"/>
          <rect x="10" y="13" width="18" height="12" fill="var(--butter)"/>
          <path d="M10 13 L19 20 L28 13 M10 25 L16 19 M28 25 L22 19" fill="none" stroke="var(--forest)" stroke-width="1.4"/>
        </svg>
        <span class="contact-text">reka.praxis@examplemail.net</span>
      </li>
    </ul>
  </div>
</div>
</body>
</html>
```